The Perfect Business Card for PineHarbor

I am looking for a business card which beautifully incorporates my logo, reflects my business and looks special, elegant and clean.

```html
<!DOCTYPE html>
<html lang="en">
<head>
<meta charset="utf-8">
<title>PineHarbor Business Card</title>
<link rel="stylesheet" href="https://fonts.googleapis.com/css2?family=Poppins:wght@400;600&display=swap">
<style>
  :root {
    --page: #e9ebe8;
    --card-white: #ffffff;
    --navy: #121d4a;
    --navy-pattern: #1a275a;
    --sky: #2f9ad6;
    --ink: #1b1f3b;
    --muted: #3a3f55;
  }
  * { margin: 0; padding: 0; box-sizing: border-box; }
  html, body {
    width: 1200px; height: 900px; overflow: hidden;
    background: var(--page);
    font-family: "Poppins", sans-serif;
  }
  .stage {
    width: 1200px; height: 900px;
    display: flex; flex-direction: column;
    align-items: center; justify-content: center; gap: 60px;
  }
  .card {
    width: 630px; height: 360px; position: relative;
    box-shadow: 0 6px 18px rgba(0,0,0,0.12);
  }
  .card-front {
    background: var(--card-white);
    display: flex; align-items: center; justify-content: center;
  }
  .identity {
    width: 250px; text-align: right; padding-right: 26px;
  }
  .identity-name {
    color: var(--sky); font-weight: 600; font-size: 22px; line-height: 1.2;
  }
  .identity-title {
    color: var(--ink); font-size: 14px; margin-top: 2px;
  }
  .divider {
    width: 2px; height: 110px; background: var(--navy);
  }
  .contacts {
    width: 290px; padding-left: 24px; list-style: none;
  }
  .contact-item {
    display: flex; align-items: center; gap: 10px;
    color: var(--muted); font-size: 14px; line-height: 1.75;
  }
  .contact-icon { width: 13px; height: 13px; flex: none; fill: var(--sky); }
  .card-back {
    background: var(--navy);
    display: flex; align-items: center; justify-content: center;
    overflow: hidden;
  }
  .back-pattern {
    position: absolute; inset: 0;
    background: radial-gradient(circle at 50% 50%, var(--navy-pattern), var(--navy) 75%);
  }
  .brand {
    position: relative; display: flex; align-items: center; gap: 16px;
  }
  .brand-circle {
    width: 70px; height: 70px; border-radius: 50%;
    border: 3px solid var(--sky);
  }
  .brand-name {
    color: var(--sky); font-size: 44px; font-weight: 400; letter-spacing: 2px;
  }
</style>
</head>
<body>
<main class="stage">
  <section class="card card-front">
    <div class="identity">
      <p class="identity-name">Daniel Vesely</p>
      <p class="identity-title">Chief Executive</p>
    </div>
    <div class="divider"></div>
    <ul class="contacts">
      <li class="contact-item">
        <svg class="contact-icon" viewBox="0 0 16 16"><path d="M3 1l3 3-2 2c1 2 3 4 5 5l2-2 3 3-2 3C6 15 1 10 1 3z"/></svg>
        +420 555 014 270
      </li>
      <li class="contact-item">
        <svg class="contact-icon" viewBox="0 0 16 16"><path d="M1 3h14v10H1z M1 3l7 6 7-6" /></svg>
        info@pineharbor.com
      </li>
      <li class="contact-item">
        <svg class="contact-icon" viewBox="0 0 16 16"><circle cx="8" cy="8" r="7" fill="none" stroke="currentColor" stroke-width="0"/><path d="M8 1a7 7 0 100 14A7 7 0 008 1zm0 2a5 5 0 110 10A5 5 0 018 3z"/><path d="M3 7.3h10v1.4H3z"/></svg>
        www.pineharbor.com
      </li>
      <li class="contact-item">
        <svg class="contact-icon" viewBox="0 0 16 16"><path d="M8 0a5.5 5.5 0 00-5.5 5.5C2.5 10 8 16 8 16s5.5-6 5.5-10.5A5.5 5.5 0 008 0zm0 8a2.5 2.5 0 110-5 2.5 2.5 0 010 5z"/></svg>
        Lipova 14, 120 00 Praha 2
      </li>
    </ul>
  </section>

  <section class="card card-back">
    <div class="back-pattern" role="img" aria-label="Faint repeating brand pattern in dark navy tones"></div>
    <div class="brand">
      <span class="brand-circle"></span>
      <span class="brand-name">PineHarbor</span>
    </div>
  </section>
</main>
</body>
</html>
```